Potato chips bag design of 85 gram for Greek and East Europe market

I want a new design for a new potato chips bag for the Greek market. The product is going to be all natural ingredient, gluten free, preservatives free, allergen free from Greek organic potatoes . Thick cut, marinated potatoes that are premium vs others. For packaging we want it to stand out on shelf. Have a Matt film . It will be called Silverbrook Tumble. Salt and Oregano flavors to start with.
Ideally to stand out on shelf we were thinking to have a black/white Color pallet and have an artistic pattern printed like the pictures attached. But of course open to ideas.
Target Market(s)
Greece and East Europe
Industry/Entity Type
Snacks Packaged goods
Requirements
Must have
- Matt film that stands out on shelf . 85 grams bag so 25cm tall and 15 cms length
Nice to have
- Ideally black/white pallet as it looks more premium. Patterns artistic that will make it look like art.
Should not have
- Traditional Pevo type of design (red-green colors etc)

```html
<!DOCTYPE html>
<html lang="en">
<head>
<meta charset="utf-8">
<title>Silverbrook Tumble – Chips Bag Front</title>
<link rel="stylesheet" href="https://fonts.googleapis.com/css2?family=Economica:wght@400;700&family=Titan+One&family=Fjalla+One&display=swap">
<style>
  :root {
    --gold: #c4a031;
    --ink: #141213;
    --paper: #ffffff;
    --stage: #ffffff;
    --pattern-dark: #0d0c0c;
    --pattern-light: #e9e7e2;
  }
  * { margin: 0; padding: 0; box-sizing: border-box; }
  html, body {
    width: 1200px; height: 591px; overflow: hidden;
    background: var(--stage);
  }
  .canvas { position: relative; width: 1200px; height: 591px; }
  .bag-front {
    position: absolute; left: 101px; top: 67px;
    width: 275px; height: 457px;
    background: var(--paper);
    overflow: hidden;
  }
  .seal-band {
    position: absolute; left: 0; top: 0; width: 100%; height: 22px;
    background: var(--gold);
  }
  .art-pattern {
    position: absolute; left: 0; top: 22px; width: 100%; height: 265px;
    background:
      linear-gradient(170deg, transparent 0 18%, rgba(233,231,226,.35) 22%, transparent 30% 48%, rgba(233,231,226,.4) 54%, transparent 62% 76%, rgba(233,231,226,.35) 82%, transparent 90%),
      linear-gradient(180deg, var(--pattern-dark), #2a2928 50%, var(--pattern-dark));
  }
  .torn-edges { position: absolute; left: 0; top: 0; width: 275px; height: 457px; }
  .claims {
    position: absolute; right: 175px; top: 329px;
    font-family: "Economica", sans-serif;
    font-size: 11.5px; line-height: 13.6px;
    color: var(--ink); text-align: right; white-space: nowrap;
  }
  .brand {
    position: absolute; left: 140px; top: 326px;
    white-space: nowrap;
  }
  .brand-name-top {
    display: block;
    font-family: "Fjalla One", sans-serif;
    font-size: 19px; line-height: 22px;
    color: var(--gold); letter-spacing: .3px;
  }
  .brand-name-main {
    display: block;
    font-family: "Titan One", sans-serif;
    font-size: 25px; line-height: 28px;
    color: var(--ink); letter-spacing: .5px;
  }
  .brand-tagline {
    display: block; margin-top: 3px;
    font-family: "Economica", sans-serif; font-weight: 700;
    font-size: 8.5px; letter-spacing: 2px;
    color: var(--ink);
  }
</style>
</head>
<body>
<main class="canvas">
  <section class="bag-front">
    <div class="seal-band"></div>
    <div class="art-pattern" role="img" aria-label="Flowing black and white abstract wave pattern artwork"></div>
    <svg class="torn-edges" viewBox="0 0 275 457" aria-hidden="true">
      <path fill="var(--gold)" d="M0 280 L34 279 L36 274 L95 273 L115 276 L170 275 L275 273 L275 290 L230 292 L180 294 L120 293 L80 296 L40 293 L18 290 L0 292 Z"/>
      <path fill="var(--paper)" d="M0 292 L18 290 L40 293 L80 296 L120 293 L180 294 L230 292 L275 290 L275 300 L0 300 Z"/>
      <path fill="var(--ink)" d="M0 427 L20 425 L34 421 L60 418 L115 419 L112 423 L150 425 L200 423 L275 422 L275 440 L200 441 L140 439 L100 440 L60 438 L20 441 L0 440 Z"/>
      <path fill="var(--gold)" d="M0 440 L20 441 L60 438 L100 440 L140 439 L200 441 L275 440 L275 457 L0 457 Z"/>
    </svg>
    <p class="claims">All natural ingredient<br>Gluten free<br>Preservatives free<br>Allergen free</p>
    <div class="brand">
      <span class="brand-name-top">Silverbrook</span>
      <span class="brand-name-main">TUMBLE</span>
      <span class="brand-tagline">Greek Organic Potatoes</span>
    </div>
  </section>
</main>
</body>
</html>
```